Harbor Self Storage

looking for a clean sharp easy to read advertising billboard to rent units

online rentals
online payment
online check out

climate control units available
competitive rates

https://www.harbor-selfstorage-example.com/

```html
<!DOCTYPE html>
<html lang="en">
<head>
<meta charset="utf-8">
<title>Harbor Self Storage – Billboard</title>
<link href="https://fonts.googleapis.com/css2?family=Montserrat:wght@600;700;800&family=Michroma&display=swap" rel="stylesheet">
<style>
  :root {
    --navy: #1b1f6b;
    --red: #ee2a31;
    --white: #ffffff;
    --page: #ffffff;
    --ink-shadow: rgba(0,0,0,0.25);
  }
  * { box-sizing: border-box; margin: 0; padding: 0; }
  html, body { width: 1200px; height: 1112px; overflow: hidden; background: var(--page); }
  .billboard {
    position: absolute; left: 20px; top: 338px; width: 1160px; height: 436px;
    background: var(--white); overflow: hidden;
    box-shadow: 0 6px 18px var(--ink-shadow);
    font-family: "Montserrat", sans-serif;
  }
  .band { position: absolute; }
  .band--top-navy { left: 0; top: 20px; width: 534px; height: 41px; background: var(--navy);
    clip-path: polygon(0 0, 97% 0, 100% 100%, 0 100%); }
  .band--headline { left: 0; top: 53px; width: 634px; height: 111px; background: var(--red);
    clip-path: polygon(0 0, 90.8% 0, 100% 100%, 0 100%); }
  .headline { position: absolute; left: 17px; top: 62px; color: var(--white);
    font-weight: 800; font-size: 44px; line-height: 44px; letter-spacing: -0.5px; }
  .features { position: absolute; left: 17px; top: 186px; list-style: none; }
  .features li { display: flex; align-items: center; height: 56px; color: var(--navy);
    font-weight: 700; font-size: 42px; letter-spacing: 0.3px; }
  .features svg { width: 46px; height: 46px; margin-right: 6px; flex: none; }
  .brand { position: absolute; left: 626px; top: 56px; width: 509px; height: 109px;
    display: flex; align-items: center; justify-content: center; gap: 14px;
    color: var(--navy); font-weight: 800; font-size: 40px; letter-spacing: 0.5px; }
  .brand__mark { width: 22px; height: 22px; background: var(--red); flex: none; }
  .perk { position: absolute; top: 282px; height: 67px; color: var(--white);
    font-weight: 800; font-size: 26px; line-height: 25px; display: flex; align-items: center; }
  .perk--climate { left: 580px; width: 343px; background: var(--red); padding-left: 40px;
    clip-path: polygon(12% 0, 100% 0, 91.5% 100%, 0 100%); }
  .perk--rates { left: 897px; width: 263px; background: var(--navy); padding-left: 35px;
    clip-path: polygon(10% 0, 100% 0, 100% 100%, 0 100%); }
  .perk__corner { position: absolute; left: 1124px; top: 282px; width: 36px; height: 67px;
    background: var(--red); clip-path: polygon(100% 0, 100% 100%, 0 100%); }
  .contact-bar { position: absolute; left: 0; top: 368px; width: 1160px; height: 68px; background: var(--navy); }
  .contact-bar__phone-panel { position: absolute; left: 0; top: 368px; width: 636px; height: 68px;
    background: var(--red); clip-path: polygon(0 0, 94.6% 0, 100% 100%, 0 100%); }
  .phone { position: absolute; left: 14px; top: 368px; height: 68px; display: flex; align-items: center;
    color: var(--white); font-family: "Michroma", sans-serif; font-size: 44px; letter-spacing: -1px; }
  .phone svg { width: 40px; height: 40px; margin-right: 8px; }
  .web { position: absolute; left: 652px; top: 368px; height: 68px; display: flex; align-items: center;
    color: var(--white); font-weight: 600; font-size: 27px; }
  .web svg { width: 28px; height: 28px; margin-right: 8px; }
  .web__tld { color: var(--red); }
</style>
</head>
<body>
<main class="billboard">
  <div class="band band--top-navy"></div>
  <div class="band band--headline"></div>
  <h1 class="headline">SAFE. SECURE. SIMPLE.<br>JUST A CLICK AWAY.</h1>

  <ul class="features">
    <li>
      <svg viewBox="0 0 48 48" fill="none" stroke="#ee2a31" stroke-width="2.5" stroke-linejoin="round">
        <rect x="7" y="10" width="34" height="24" rx="2"/><path d="M3 38h42l-3 4H6z"/>
        <path d="M16 30V21l8-6 8 6v9z"/><rect x="21" y="23" width="6" height="7"/>
      </svg>ONLINE RENTALS</li>
    <li>
      <svg viewBox="0 0 48 48" fill="none" stroke="#ee2a31" stroke-width="2.5">
        <rect x="10" y="4" width="22" height="40" rx="3"/><circle cx="24" cy="24" r="8"/>
        <path d="M26 20h-3a2 2 0 0 0 0 4h2a2 2 0 0 1 0 4h-3M24 18v2M24 28v2"/>
        <path d="M36 16a6 6 0 0 1 0 8M40 13a10 10 0 0 1 0 14"/>
      </svg>ONLINE PAYMENT</li>
    <li>
      <svg viewBox="0 0 48 48" fill="none" stroke="#ee2a31" stroke-width="2.5" stroke-linejoin="round">
        <path d="M3 14h6l5 20h20l4-14H12"/><circle cx="16" cy="40" r="3"/><circle cx="31" cy="40" r="3"/>
        <circle cx="35" cy="11" r="9"/><path d="M31 11l3 3 5-6"/>
      </svg>ONLINE CHECK OUT</li>
  </ul>

  <div class="brand"><span class="brand__mark"></span>HARBOR SELF STORAGE</div>

  <div class="perk perk--climate">CLIMATE CONTROL<br>UNITS AVAILABLE</div>
  <div class="perk perk--rates">COMPETITIVE<br>RATES</div>
  <div class="perk__corner"></div>

  <div class="contact-bar"></div>
  <div class="contact-bar__phone-panel"></div>
  <div class="phone">
    <svg viewBox="0 0 48 48" fill="none" stroke="#ffffff" stroke-width="3.5" stroke-linecap="round">
      <path d="M12 6l7 9-4 4c2 6 7 11 13 13l4-4 9 7-4 6C22 41 7 26 6 11z" fill="#ffffff"/>
      <path d="M28 6a14 14 0 0 1 14 14M28 13a7 7 0 0 1 7 7"/>
    </svg>555-010-4000</div>
  <div class="web">
    <svg viewBox="0 0 32 32" fill="none" stroke="#ee2a31" stroke-width="2">
      <circle cx="16" cy="16" r="13"/><ellipse cx="16" cy="16" rx="6" ry="13"/>
      <path d="M3 16h26M5 9h22M5 23h22"/>
    </svg>harbor-selfstorage-example<span class="web__tld">.com</span></div>
</main>
</body>
</html>
```